Movie Showtimes Website needs an updated new look

Website = www.frametally.net

We want to update the look of our website. We want our website to look modern, trendy, something that was designed in 2018.

We don't need any HTML or CSS or web development. All we need is the graphical prototype, preferably in Photoshop with layers.

Most of our visitors use mobile devices. Our website is RESPONSIVE -- it is flexible to fit all screen sizes.

We will use this new logo (designed on PixelGuild):
https://www.pixelguild.net/design/52937461

Thank you for your kind consideration.

Please find attached 3 PDF files with the current webpages:

1. Each city location has its own HOME PAGE like this:

https://www.frametally.net/ont/ottawa/

2. The most visited pages have movie SHOWTIMES and look like this:

https://www.frametally.net/theatres/marquee-birchfield-lux

MOVIE TITLE (poster + basic info + 4 buttons)
-- the type of the screening (ex. Regular, IMAX, 3D, etc.)
-- individual days and showtimes

3. INFORMATION about movies:

https://www.frametally.net/movies/glass-harbor-run-2018

Thank you.

Target Market(s)

Canada and USA, target audience = ages 13-50

Industry/Entity Type

Movie

Number of Pages Required

3 page

Font styles to use
Sans Serif

Colors

Designer to choose colors to be used in the design.

Requirements
Must have
• - For the main body text (such as movie times, description, information) we prefer dark text on a light background.
• - We will use the new logo https://www.pixelguild.net/design/52937461 -- but the text Frame Tally in the logo doesn't have to look exactly like that, it can be on the same line and have the same or different size
Should not have
• No more than 2 different fonts (ex. one font for headers and titles, another one for text)

```html
<!DOCTYPE html>
<html lang="en">
<head>
<meta charset="utf-8">
<title>Frame Tally – Home</title>
<link rel="stylesheet" href="https://fonts.googleapis.com/css2?family=Poppins:ital,wght@0,400;0,500;0,600;0,700;1,600;1,700&display=swap">
<style>
  :root {
    --page: #f3f5f9;
    --white: #ffffff;
    --ink: #2b2d31;
    --muted: #7c8088;
    --bar: #3c3d40;
    --bar-dark: #2a2b2e;
    --blue: #3aa3ef;
    --blue-soft: #e6f3fd;
    --line: #dde1e7;
    --ad-black: #0d0d0d;
    --orange: #f7851e;
    --gold: #f5b52a;
  }
  * { box-sizing: border-box; margin: 0; padding: 0; }
  html, body { width: 1200px; height: 900px; overflow: hidden; }
  body {
    background: var(--page);
    font-family: "Poppins", sans-serif;
    color: var(--ink);
  }
  .site { width: 1200px; height: 900px; position: relative; }

  /* Header */
  .site-header {
    height: 78px; background: var(--white);
    display: flex; align-items: center;
    padding: 0 110px;
  }
  .brand { display: flex; align-items: center; gap: 10px; }
  .brand-dot { width: 26px; height: 26px; border-radius: 50%; background: var(--blue); }
  .brand-name { font-size: 22px; font-weight: 700; color: var(--ink); letter-spacing: .5px; }
  .header-tools { margin-left: auto; display: flex; align-items: center; gap: 14px; }
  .search {
    width: 300px; height: 32px; border: 1px solid var(--line); border-radius: 16px;
    display: flex; align-items: center; justify-content: space-between;
    padding: 0 4px 0 16px; font-size: 12px; color: var(--muted);
  }
  .search-btn {
    width: 24px; height: 24px; border-radius: 50%; background: var(--bar-dark);
    display: flex; align-items: center; justify-content: center;
  }
  .login {
    height: 30px; padding: 0 18px; border-radius: 15px; background: var(--blue);
    color: var(--white); font-size: 11px; font-weight: 600; letter-spacing: .5px;
    display: flex; align-items: center; gap: 6px;
  }
  .lang {
    height: 30px; width: 130px; border: 1px solid var(--blue); border-radius: 15px;
    padding: 0 14px; font-size: 11px; font-weight: 500;
    display: flex; align-items: center; justify-content: space-between;
  }

  /* Nav */
  .main-nav {
    margin: 0 110px; height: 36px; background: var(--bar);
    display: flex; align-items: center; justify-content: space-between; padding: 0 26px;
  }
  .main-nav a {
    color: var(--white); text-decoration: none; font-size: 11px; font-weight: 600;
    letter-spacing: 1.5px; text-transform: uppercase; position: relative;
  }
  .main-nav a.is-active { color: var(--blue); }
  .main-nav a.is-active::after {
    content: ""; position: absolute; left: 0; right: 0; bottom: -11px; height: 3px; background: var(--blue);
  }
  .nav-sep { width: 1px; height: 12px; background: #6b6d72; }

  /* Leaderboard ad */
  .ad-leader {
    margin: 14px 110px 0; height: 64px; background: var(--ad-black);
    display: flex; align-items: center; padding: 0 30px; gap: 30px;
  }
  .ad-brand { color: var(--orange); font-size: 17px; font-weight: 700; }
  .ad-art {
    width: 170px; height: 56px; border-radius: 4px;
    background: radial-gradient(circle, #f6c343 0%, #b4600f 40%, #1a0e05 75%);
  }
  .ad-slogan { color: var(--white); font-size: 18px; font-weight: 700; font-style: italic; line-height: 1.05; }
  .ad-slogan span { color: var(--gold); }
  .ad-cta {
    margin-left: auto; background: var(--orange); color: var(--white);
    font-size: 13px; font-weight: 700; text-align: center; line-height: 1.1;
    padding: 8px 22px; border-radius: 18px;
  }

  /* Columns */
  .content { display: flex; gap: 20px; margin: 16px 110px 0; }
  .main-col { width: 760px; }
  .side-col { width: 200px; }

  .section-bar {
    height: 40px; background: var(--bar); color: var(--white);
    font-size: 15px; font-weight: 600; display: flex; align-items: center; justify-content: center;
  }
  .panel { background: var(--white); }
  .finder { display: flex; gap: 20px; padding: 20px 26px 24px; }
  .finder-btn {
    flex: 1; height: 42px; border-radius: 21px; border: 2px solid var(--blue);
    font-size: 11px; font-weight: 600; letter-spacing: 1px; text-transform: uppercase;
    display: flex; align-items: center; justify-content: center; color: var(--blue);
  }
  .finder-btn.is-primary { background: var(--blue); color: var(--white); }

  .new-movies { margin-top: 18px; }
  .movie-card { display: flex; gap: 30px; padding: 20px 26px 24px; }
  .poster {
    width: 190px; height: 290px; flex-shrink: 0; position: relative;
    background: linear-gradient(180deg, #3f4a4e 0%, #1f2628 55%, #0e1213 100%);
  }
  .poster-tag {
    position: absolute; top: 10px; left: 10px; background: var(--orange);
    color: var(--white); font-size: 10px; font-weight: 700; padding: 2px 8px;
  }
  .movie-info { flex: 1; display: flex; flex-direction: column; }
  .movie-top { display: flex; justify-content: space-between; align-items: flex-start; }
  .movie-title { font-size: 22px; font-weight: 500; }
  .movie-date { font-size: 12px; color: var(--blue); margin-top: 2px; }
  .rating { display: flex; align-items: center; gap: 8px; font-size: 11px; color: var(--muted); }
  .rating-pill {
    background: var(--blue); color: var(--white); font-size: 11px; font-weight: 600;
    padding: 3px 14px; border-radius: 12px;
  }
  .facts { margin-top: 20px; border-collapse: collapse; font-size: 12px; }
  .facts th {
    text-align: left; font-weight: 600; font-size: 11px; letter-spacing: .5px;
    text-transform: uppercase; width: 150px; padding: 7px 0; border-right: 1px solid var(--line);
  }
  .facts td { padding: 7px 0 7px 24px; color: var(--muted); }
  .card-actions { margin-top: auto; display: flex; gap: 14px; }
  .card-btn {
    width: 100px; height: 32px; border: 2px solid #c9cdd3; border-radius: 16px;
    font-size: 12px; display: flex; align-items: center; justify-content: center;
  }
  .card-btn.is-active { border-color: var(--blue); color: var(--blue); background: var(--blue-soft); }

  .ad-sky {
    height: 470px; background: var(--ad-black);
    display: flex; flex-direction: column; align-items: center; padding: 24px 14px; gap: 20px;
  }
  .ad-sky .ad-art { width: 172px; height: 220px; border-radius: 50%; }
  .ad-sky .ad-slogan { text-align: center; font-size: 17px; }
  .ad-sky .ad-cta { margin: 0; font-size: 11px; padding: 8px 16px; }
  .ad-promo {
    margin-top: 16px; height: 200px;
    background: linear-gradient(160deg, #f6b13c 0%, #e9894a 55%, #7b3fa0 100%);
  }
</style>
</head>
<body>
<div class="site">
  <header class="site-header">
    <div class="brand">
      <span class="brand-dot"></span>
      <span class="brand-name">Frame Tally</span>
    </div>
    <div class="header-tools">
      <div class="search">Search
        <span class="search-btn">
          <svg width="12" height="12" viewBox="0 0 12 12"><circle cx="5" cy="5" r="3.5" fill="none" stroke="#fff" stroke-width="1.5"/><line x1="7.6" y1="7.6" x2="10.5" y2="10.5" stroke="#fff" stroke-width="1.5"/></svg>
        </span>
      </div>
      <div class="login">
        <svg width="10" height="10" viewBox="0 0 10 10"><circle cx="5" cy="3" r="2.2" fill="#fff"/><path d="M1 10a4 4 0 0 1 8 0z" fill="#fff"/></svg>
        LOGIN
      </div>
      <div class="lang">Français
        <svg width="8" height="6" viewBox="0 0 8 6"><path d="M0 0h8L4 6z" fill="#2b2d31"/></svg>
      </div>
    </div>
  </header>

  <nav class="main-nav">
    <a class="is-active" href="#">Home</a><span class="nav-sep"></span>
    <a href="#">Cinemas</a><span class="nav-sep"></span>
    <a href="#">Movies</a><span class="nav-sep"></span>
    <a href="#">Top 10</a><span class="nav-sep"></span>
    <a href="#">Trailers</a><span class="nav-sep"></span>
    <a href="#">Upcoming</a><span class="nav-sep"></span>
    <a href="#">DVD</a><span class="nav-sep"></span>
    <a href="#">More</a>
  </nav>

  <aside class="ad-leader">
    <span class="ad-brand">Coinvault</span>
    <div class="ad-art" role="img" aria-label="Glowing gold coin in a burst of light"></div>
    <p class="ad-slogan"><span>JOIN THE</span><br>REVOLUTION</p>
    <span class="ad-cta">REGISTER<br>FOR FREE</span>
  </aside>

  <div class="content">
    <main class="main-col">
      <section class="movie-time">
        <h2 class="section-bar">Movie Time</h2>
        <div class="panel finder">
          <span class="finder-btn">Choose a Cinema</span>
          <span class="finder-btn is-primary">Choose a Movie</span>
        </div>
      </section>

      <section class="new-movies">
        <h2 class="section-bar">New Movies This Week</h2>
        <article class="panel movie-card">
          <div class="poster" role="img" aria-label="Movie poster: a dim farmhouse interior with a figure at a window">
            <span class="poster-tag">14A</span>
          </div>
          <div class="movie-info">
            <div class="movie-top">
              <div>
                <h3 class="movie-title">A Silent Field</h3>
                <p class="movie-date">In theatres April 6, 2018</p>
              </div>
              <div class="rating">Rating <span class="rating-pill">72 %</span></div>
            </div>
            <table class="facts">
              <tr><th>Year</th><td>2018</td></tr>
              <tr><th>Run time</th><td>1h 30m</td></tr>
              <tr><th>Genre</th><td>Horror/Thriller</td></tr>
              <tr><th>Directed by</th><td>Jon Mercer</td></tr>
              <tr><th>Company</th><td>Summit Ridge Pictures</td></tr>
            </table>
            <div class="card-actions">
              <span class="card-btn">Times</span>
              <span class="card-btn is-active">Info</span>
              <span class="card-btn">Videos</span>
              <span class="card-btn">Reviews</span>
            </div>
          </div>
        </article>
      </section>
    </main>

    <aside class="side-col">
      <div class="ad-sky">
        <span class="ad-brand">Coinvault</span>
        <div class="ad-art" role="img" aria-label="Gold coin glowing in an orange light burst"></div>
        <p class="ad-slogan"><span>JOIN THE</span><br>REVOLUTION</p>
        <span class="ad-cta">FREE REGISTRATION</span>
      </div>
      <div class="ad-promo" role="img" aria-label="Film promotion banner with hand-lettered title on yellow and purple"></div>
    </aside>
  </div>
</div>
</body>
</html>
```